Ironvale Leasing Corp - Business Card Design

Need a new modern designed business card that is different and stands out to represent my equipment financing company. Ironvale Leasing Corp finances all types of equipment and all types of industries. We like to do equipment financing a different way by putting customers first and want our card to represent that different approach to business. I want a card that some remembers when they receive it so it sticks in their mind and makes that wow impression.

Card should have a black background so the logo stands out. It can be horizontial or vertical or a combination of both.

Front of card information is below that shows the information that would go on my card. That is where I want a different look or design to stand out. The front could be split black/orange colour so the logo could pop on black side and information on orange side with different lettering. Just outside the box thinking on the front of the card. Open to any type of design.

Back of card is below which i I like unless you have a different spin to provide or a different idea that would make the card better as I am open to anything that looks great.

Target Market(s)

Ironvale Leasing Corp deals with business owners in all industries.

Industry/Entity Type

Business

Contact Information for Business Card

Colors

Designer to choose colors to be used in the design.

Requirements
Must have
• Modern
• Different
• Stand Out
• Makes an Impression

```html
<!DOCTYPE html>
<html lang="en">
<head>
<meta charset="utf-8">
<title>Ironvale Leasing Corp – Business Card</title>
<link rel="stylesheet" href="https://fonts.googleapis.com/css2?family=Lato:wght@400;700&display=swap">
<style>
  :root {
    --stage: #2f2f30;
    --orange-top: #f7891f;
    --orange-bottom: #ee3b24;
    --ink: #000000;
    --white: #ffffff;
    --card-w: 856px;
    --card-h: 488px;
    --corner: 49px;
  }
  * { margin: 0; padding: 0; box-sizing: border-box; }
  html, body {
    width: 1189px;
    height: 1200px;
    overflow: hidden;
    background: var(--stage);
    font-family: "Lato", Arial, sans-serif;
  }
  .card {
    position: absolute;
    left: 171px;
    width: var(--card-w);
    height: var(--card-h);
    overflow: hidden;
  }

  /* Front */
  .card-front {
    top: 67px;
    border-top-left-radius: var(--corner);
    background: linear-gradient(to bottom, var(--orange-top), var(--orange-bottom));
  }
  .front-brand {
    position: absolute;
    left: 0;
    right: 0;
    top: 196px;
    display: flex;
    flex-direction: column;
    align-items: center;
    gap: 16px;
  }
  .front-brand .brand-dot {
    width: 34px;
    height: 34px;
    border-radius: 50%;
    background: var(--ink);
  }
  .front-brand .brand-name {
    font-weight: 700;
    font-size: 40px;
    letter-spacing: 1px;
    color: var(--ink);
  }
  .front-web {
    position: absolute;
    left: 0;
    right: 0;
    top: 374px;
    text-align: center;
    font-size: 19px;
    letter-spacing: 2.6px;
    color: var(--ink);
  }

  /* Back */
  .card-back {
    top: 626px;
    border-top-right-radius: var(--corner);
    background: var(--ink);
  }
  .back-brand {
    position: absolute;
    left: 60px;
    width: 320px;
    top: 150px;
    display: flex;
    flex-direction: column;
    align-items: center;
    gap: 18px;
  }
  .back-brand .brand-dot {
    width: 40px;
    height: 40px;
    border-radius: 50%;
    background: var(--orange-top);
  }
  .back-brand .brand-name {
    font-weight: 400;
    font-size: 33px;
    line-height: 1.15;
    letter-spacing: 2px;
    text-align: center;
    text-transform: uppercase;
    color: var(--orange-top);
  }
  .person {
    position: absolute;
    left: 455px;
    top: 116px;
    color: var(--white);
  }
  .person-name {
    font-weight: 700;
    font-size: 29px;
    line-height: 1;
  }
  .person-title {
    font-size: 23px;
    margin-top: 6px;
  }
  .contact {
    position: absolute;
    left: 457px;
    top: 290px;
    color: var(--white);
    font-size: 22px;
    line-height: 29px;
  }
  .web-band {
    position: absolute;
    left: 0;
    right: 0;
    top: 419px;
    height: 41px;
    background: linear-gradient(to bottom, var(--orange-top), var(--orange-bottom));
    display: flex;
    align-items: center;
    justify-content: center;
    font-size: 19px;
    letter-spacing: 2.6px;
    color: var(--ink);
  }
</style>
</head>
<body>
  <section class="card card-front" aria-label="Card front">
    <div class="front-brand">
      <span class="brand-dot"></span>
      <span class="brand-name">Ironvale Leasing Corp</span>
    </div>
    <p class="front-web">www.ironvaleleasing.ca</p>
  </section>

  <section class="card card-back" aria-label="Card back">
    <div class="back-brand">
      <span class="brand-dot"></span>
      <span class="brand-name">Ironvale<br>Leasing Corp</span>
    </div>
    <div class="person">
      <p class="person-name">DEAN MARLOW</p>
      <p class="person-title">PRESIDENT</p>
    </div>
    <div class="contact">
      <p>403.555.0192</p>
      <p>dean@ironvaleleasing.ca</p>
    </div>
    <div class="web-band">www.ironvaleleasing.ca</div>
  </section>
</body>
</html>
```